VerdaMetrix PowerPoint Presentation Design

I am looking for a PowerPoint design for a new company based in Dallas, Texas called VerdaMetrix. We provide extremely powerful predictive and prescriptive analytics software focused on the Internet of Things (IoT) market. Our initial products are called VMX Foundry and VMX Pulse. We would like to see designs that support our logo design, which is attached.

I AM LOOKING FOR A THEME TO BE DEVELOPED FOR THE TITLE SLIDE AND INSIDE SLIDES OF A PRESENTATION. I AM NOT LOOKING FOR SOMEONE TO TAKE MY CONTENT AND CREATE A COMPLETE PRESENTATION.

Target Market(s)

Advanced Analytics, Internet of Things

Industry/Entity Type

It Company

Requirements
Must have
• Bolder colors, but they must work with the logo
Nice to have
• I prefer that the design incorporate the them of "connectivity" or "connectedness" to reflect the IoT market and "intelligence" or "smart" to reflect the analytics aspect of the business
Should not have
• I don't want people represented in the graphics scheme

```html
<!DOCTYPE html>
<html lang="en">
<head>
<meta charset="utf-8">
<title>VerdaMetrix Presentation Theme</title>
<link rel="stylesheet" href="https://fonts.googleapis.com/css2?family=Montserrat:wght@500;700&family=Quicksand:wght@500&family=Titillium+Web:wght@400;600&display=swap">
<style>
  :root {
    --stage: #000000;
    --brand-blue: #0d3fa3;
    --deep-blue: #0a2f8f;
    --bright-blue: #1e5fd0;
    --accent-orange: #fca90a;
    --paper: #ffffff;
    --mist: #eeeeef;
    --charcoal: #333333;
    --icon-gray: #7a7a7a;
    --body-gray: #6e6e6e;
    --rule-gray: #9aa3b5;
  }
  * { box-sizing: border-box; margin: 0; padding: 0; }
  html, body { width: 1068px; height: 1200px; overflow: hidden; background: var(--stage); }
  .canvas { position: relative; width: 1068px; height: 1200px; background: var(--stage); overflow: hidden; font-family: "Titillium Web", sans-serif; }
  .slide { position: absolute; width: 516px; height: 387px; overflow: hidden; background: var(--paper); }
  .slide--title { left: 9px; top: 9px; }
  .slide--feature { left: 535px; top: 9px; }
  .slide--list { left: 9px; top: 408px; }
  .slide--columns { left: 535px; top: 408px; }
  .slide--section { left: 9px; top: 803px; }

  /* Title slide */
  .hero-photo { position: absolute; left: 0; top: 0; width: 100%; height: 239px;
    background: linear-gradient(135deg, #3f78c4 0%, #2a62b8 45%, #1e56ad 100%); }
  .hero-heading { position: absolute; left: 0; right: 0; top: 117px; text-align: center; color: var(--paper);
    font-family: "Montserrat", sans-serif; font-weight: 700; font-size: 25px; letter-spacing: 0.5px; }
  .hero-sub { position: absolute; left: 0; right: 0; top: 152px; text-align: center; color: var(--paper);
    font-family: "Titillium Web", sans-serif; font-size: 21px; }
  .brand-band { position: absolute; left: 0; top: 239px; width: 100%; height: 124px; background: var(--mist); }
  .brand-name { position: absolute; left: 0; right: 0; top: 272px; text-align: center; color: var(--brand-blue);
    font-family: "Titillium Web", sans-serif; font-weight: 600; font-size: 46px; line-height: 1; }
  .accent-rule { position: absolute; left: 0; top: 363px; width: 100%; height: 3px; background: var(--accent-orange); }
  .base-band { position: absolute; left: 0; top: 366px; width: 100%; height: 21px; background: var(--charcoal); }

  /* Feature slide */
  .feature-photo { position: absolute; inset: 0;
    background: radial-gradient(circle at 50% 35%, #1f5ec7 0%, #1447b3 45%, #0c3aa0 100%); }
  .badge { position: absolute; left: 225px; top: 144px; }
  .feature-heading { position: absolute; left: 0; right: 0; top: 226px; text-align: center; color: var(--paper);
    font-family: "Quicksand", sans-serif; font-weight: 500; font-size: 19px; letter-spacing: 0.4px; }
  .feature-sub { position: absolute; left: 0; right: 0; top: 254px; text-align: center; color: var(--paper);
    font-family: "Quicksand", sans-serif; font-weight: 500; font-size: 18px; }

  /* Content slides */
  .slide-header { position: absolute; left: 0; top: 0; width: 100%; height: 40px; background: var(--brand-blue);
    border-bottom: 2px solid var(--rule-gray); }
  .slide-header__title { position: absolute; left: 9px; top: 5px; color: var(--paper); font-weight: 600; font-size: 20px; }
  .slide-header__brand { position: absolute; right: 6px; top: 3px; color: var(--paper); font-weight: 600; font-size: 24px; line-height: 1.3; }
  .slide-footer { position: absolute; left: 0; bottom: 0; width: 100%; height: 23px; background: var(--accent-orange);
    color: var(--paper); font-size: 9px; border-top: 1px solid #2a2a2a; }
  .slide-footer__copy { position: absolute; left: 5px; top: 4px; }
  .slide-footer__page { position: absolute; right: 4px; top: 5px; }

  .list-item { position: absolute; left: 0; width: 100%; }
  .list-item__icon { position: absolute; left: 38px; width: 46px; height: 46px; border-radius: 50%; background: var(--icon-gray);
    display: flex; align-items: center; justify-content: center; }
  .list-item__title { position: absolute; left: 101px; top: 0; color: var(--brand-blue); font-weight: 600; font-size: 13px; }
  .list-item__body { position: absolute; left: 101px; top: 19px; width: 405px; color: var(--body-gray); font-size: 8.4px; line-height: 14px; }

  .column { position: absolute; top: 98px; width: 150px; text-align: center; }
  .column__icon { width: 46px; height: 46px; margin: 0 auto; border-radius: 50%; background: var(--bright-blue);
    display: flex; align-items: center; justify-content: center; }
  .column__title { margin-top: 7px; color: var(--brand-blue); font-weight: 600; font-size: 13px; line-height: 18px; }
  .column__body { margin-top: 2px; color: var(--body-gray); font-size: 8.4px; line-height: 14.2px; padding: 0 5px; }

  /* Section slide */
  .section-backdrop { position: absolute; inset: 0;
    background: linear-gradient(120deg, #1543b0 0%, #0f3aa6 50%, #1a4cb8 100%); }
  .section-alert { position: absolute; left: 233px; top: 165px; }
  .section-rule { position: absolute; left: 182px; top: 231px; width: 182px; height: 1.5px; background: var(--paper); }
  .section-title { position: absolute; left: 0; right: 0; top: 236px; text-align: center; color: var(--paper);
    font-weight: 600; font-size: 19px; }
</style>
</head>
<body>
<main class="canvas">

  <section class="slide slide--title">
    <div class="hero-photo" role="img" aria-label="Blue-toned photo of hands using a tablet with analytics charts"></div>
    <h1 class="hero-heading">Welcome Message</h1>
    <p class="hero-sub">Sub title here</p>
    <div class="brand-band"></div>
    <p class="brand-name">VerdaMetrix</p>
    <div class="accent-rule"></div>
    <div class="base-band"></div>
  </section>

  <section class="slide slide--feature">
    <div class="feature-photo" role="img" aria-label="Blue-toned photo of connected device icons around a central laptop"></div>
    <svg class="badge" width="66" height="66" viewBox="0 0 66 66" aria-hidden="true">
      <circle cx="33" cy="33" r="32" fill="#1447b3" stroke="#6f9be6" stroke-width="1"/>
      <circle cx="37" cy="19" r="4" fill="#fff"/>
      <path d="M27 29 h11 l-5 18 q-1 3 2 2 l3 -1 l-1 3 q-6 3 -10 2 q-3 -1 -2 -5 l4 -14 h-3 z" fill="#fff"/>
    </svg>
    <h2 class="feature-heading">Creative Single Image Portfolio Options</h2>
    <p class="feature-sub">Sub title here</p>
  </section>

  <section class="slide slide--list">
    <header class="slide-header">
      <h2 class="slide-header__title">Project Title Here</h2>
      <span class="slide-header__brand">VerdaMetrix</span>
    </header>

    <div class="list-item" style="top:90px">
      <div class="list-item__icon" style="top:-5px">
        <svg width="16" height="16" viewBox="0 0 16 16" aria-hidden="true"><rect x="1" y="1" width="14" height="14" rx="2" fill="#fff"/><path d="M4 8 l3 3 l5 -6" stroke="#7a7a7a" stroke-width="2" fill="none"/></svg>
      </div>
      <h3 class="list-item__title">Text Titlte Here</h3>
      <p class="list-item__body">Lorem ipsum dolor sit Lorem ipsum dolor sit&nbsp; Lorem ipsum dolor sit Lorem ipsum dolor sit&nbsp; Lorem ipsum dolor sit Lorem ipsum dolor sit&nbsp; Lorem ipsum dolor sit Lorem ipsum dolor sit&nbsp; Lorem ipsum dolor sit Lorem ipsum dolor sit Lorem ipsum dolor sit&nbsp; Lorem ipsum dolor sit Lorem ipsum dolor sit&nbsp; Lorem ipsum dolor sit Lorem ipsum dolor sit</p>
    </div>

    <div class="list-item" style="top:168px">
      <div class="list-item__icon" style="top:-5px;left:35px">
        <svg width="18" height="12" viewBox="0 0 18 12" aria-hidden="true"><rect x="0.5" y="1" width="17" height="10" rx="5" fill="#fff"/><path d="M4 6 h4 M6 4 v4" stroke="#7a7a7a" stroke-width="1.4"/><circle cx="12" cy="5" r="1" fill="#7a7a7a"/><circle cx="14" cy="7" r="1" fill="#7a7a7a"/></svg>
      </div>
      <h3 class="list-item__title">Text Titlte Here</h3>
      <p class="list-item__body">Lorem ipsum dolor sit Lorem ipsum dolor sit&nbsp; Lorem ipsum dolor sit Lorem ipsum dolor sit&nbsp; Lorem ipsum dolor sit Lorem ipsum dolor sit&nbsp; Lorem ipsum dolor sit Lorem ipsum dolor sit&nbsp; Lorem ipsum dolor sit Lorem ipsum dolor sit Lorem ipsum dolor sit&nbsp; Lorem ipsum dolor sit Lorem ipsum dolor sit&nbsp; Lorem ipsum dolor sit Lorem ipsum dolor sit</p>
    </div>

    <div class="list-item" style="top:259px">
      <div class="list-item__icon" style="top:-7px;left:37px">
        <svg width="18" height="16" viewBox="0 0 18 16" aria-hidden="true"><rect x="1" y="1" width="16" height="10" rx="1" fill="#fff"/><rect x="7" y="11" width="4" height="3" fill="#fff"/><rect x="4" y="14" width="10" height="1.5" fill="#fff"/></svg>
      </div>
      <h3 class="list-item__title">Text Titlte Here</h3>
      <p class="list-item__body">Lorem ipsum dolor sit Lorem ipsum dolor sit&nbsp; Lorem ipsum dolor sit Lorem ipsum dolor sit&nbsp; Lorem ipsum dolor sit Lorem ipsum dolor sit&nbsp; Lorem ipsum dolor sit Lorem ipsum dolor sit&nbsp; Lorem ipsum dolor sit Lorem ipsum dolor sit Lorem ipsum dolor sit&nbsp; Lorem ipsum dolor sit Lorem ipsum dolor sit&nbsp; Lorem ipsum dolor sit Lorem ipsum dolor sit</p>
    </div>

    <footer class="slide-footer">
      <span class="slide-footer__copy">Copyright text here</span>
      <span class="slide-footer__page">Page :01</span>
    </footer>
  </section>

  <section class="slide slide--columns">
    <header class="slide-header">
      <h2 class="slide-header__title">Project Title Here</h2>
      <span class="slide-header__brand">VerdaMetrix</span>
    </header>

    <div class="column" style="left:12px">
      <div class="column__icon">
        <svg width="16" height="16" viewBox="0 0 16 16" aria-hidden="true"><rect x="1" y="1" width="14" height="14" rx="2" fill="#fff"/><path d="M4 8 l3 3 l5 -6" stroke="#1e5fd0" stroke-width="2" fill="none"/></svg>
      </div>
      <h3 class="column__title">Text Titlte Here</h3>
      <p class="column__body">Lorem ipsum dolor sit Lorem ipsum dolor sit&nbsp; Lorem ipsum dolor sit Lorem ipsum dolor sit&nbsp; Lorem ipsum dolor sit Lorem ipsum dolor sit Lorem ipsum dolor sit&nbsp; Lorem ipsum dolor sit Lorem ipsum dolor sit&nbsp; Lorem ipsum dolor sit Lorem ipsum dolor sit Lorem ipsum dolor sit Lorem ipsum dolor sit</p>
    </div>

    <div class="column" style="left:184px">
      <div class="column__icon" style="transform:translateY(-2px)">
        <svg width="18" height="16" viewBox="0 0 18 16" aria-hidden="true"><rect x="1" y="1" width="16" height="10" rx="1" fill="#fff"/><rect x="7" y="11" width="4" height="3" fill="#fff"/><rect x="4" y="14" width="10" height="1.5" fill="#fff"/></svg>
      </div>
      <h3 class="column__title">Text Titlte Here</h3>
      <p class="column__body">Lorem ipsum dolor sit Lorem ipsum dolor sit&nbsp; Lorem ipsum dolor sit Lorem ipsum dolor sit&nbsp; Lorem ipsum dolor sit Lorem ipsum dolor sit Lorem ipsum dolor sit&nbsp; Lorem ipsum dolor sit Lorem ipsum dolor sit&nbsp; Lorem ipsum dolor sit Lorem ipsum dolor sit Lorem ipsum dolor sit Lorem ipsum dolor sit</p>
    </div>

    <div class="column" style="left:356px">
      <div class="column__icon">
        <svg width="18" height="12" viewBox="0 0 18 12" aria-hidden="true"><rect x="0.5" y="1" width="17" height="10" rx="5" fill="#fff"/><path d="M4 6 h4 M6 4 v4" stroke="#1e5fd0" stroke-width="1.4"/><circle cx="12" cy="5" r="1" fill="#1e5fd0"/><circle cx="14" cy="7" r="1" fill="#1e5fd0"/></svg>
      </div>
      <h3 class="column__title">Text Titlte Here</h3>
      <p class="column__body">Lorem ipsum dolor sit Lorem ipsum dolor sit&nbsp; Lorem ipsum dolor sit Lorem ipsum dolor sit&nbsp; Lorem ipsum dolor sit Lorem ipsum dolor sit Lorem ipsum dolor sit&nbsp; Lorem ipsum dolor sit Lorem ipsum dolor sit&nbsp; Lorem ipsum dolor sit Lorem ipsum dolor sit Lorem ipsum dolor sit Lorem ipsum dolor sit</p>
    </div>

    <footer class="slide-footer">
      <span class="slide-footer__copy">Copyright text here</span>
      <span class="slide-footer__page">Page :01</span>
    </footer>
  </section>

  <section class="slide slide--section">
    <div class="section-backdrop" role="img" aria-label="Deep blue backdrop with a faint honeycomb texture"></div>
    <svg class="section-alert" width="52" height="52" viewBox="0 0 52 52" aria-hidden="true">
      <circle cx="26" cy="26" r="26" fill="#fff"/>
      <rect x="22.5" y="9" width="7" height="23" rx="1.5" fill="#0f3aa6"/>
      <rect x="22.5" y="36" width="7" height="7" rx="1" fill="#0f3aa6"/>
    </svg>
    <div class="section-rule"></div>
    <h2 class="section-title">Section TItle Here</h2>
  </section>

</main>
</body>
</html>
```